New Business Card Design Project

The legal name of the company is TTTolvane, we also refer to it as simply Tolvane or you could also use the initials TTT...... please feel creative.
Excellent design.
On the second side, if you could image North and South America on each drop of water ... it almost looks like that now.
The website is www.tttolvane.com
Attached is another card with the required information; no addresses.

Industry/Entity Type

Legal

```html
<!DOCTYPE html>
<html lang="en">
<head>
<meta charset="utf-8">
<title>TTTolvane — Business Card</title>
<link rel="stylesheet" href="https://fonts.googleapis.com/css2?family=Quicksand:wght@400;500&display=swap">
<style>
  :root {
    --navy: #13293d;
    --paper: #ffffff;
    --stage: #f1f2f3;
    --ink: #1a2330;
    --stone: #a9adb2;
    --stone-light: #c9ccd0;
    --band-text: #aab6c2;
  }
  * { box-sizing: border-box; margin: 0; padding: 0; }
  html, body { width: 1200px; height: 873px; overflow: hidden; }
  body {
    background: var(--stage);
    font-family: "Quicksand", sans-serif;
    color: var(--ink);
    display: flex;
    align-items: center;
    justify-content: center;
    gap: 60px;
  }
  .card {
    position: relative;
    width: 520px;
    height: 300px;
    overflow: hidden;
    box-shadow: 0 6px 18px rgba(0,0,0,0.12);
  }

  /* Front */
  .card--front { background: var(--paper); }
  .card__map {
    position: absolute;
    left: 250px; top: 0;
    width: 270px; height: 300px;
    background: linear-gradient(160deg, var(--stone-light) 0%, var(--stone) 60%, var(--stone-light) 100%);
  }
  .wordmark {
    position: absolute;
    left: 34px; top: 26px;
  }
  .wordmark__name {
    font-size: 46px;
    font-weight: 500;
    letter-spacing: 4px;
    color: var(--navy);
    line-height: 1;
  }
  .wordmark__rule {
    width: 240px;
    height: 1px;
    background: var(--ink);
    margin-top: 6px;
  }
  .wordmark__legal {
    font-size: 17px;
    font-weight: 400;
    color: var(--ink);
    margin-top: 3px;
    padding-left: 70px;
  }
  .contact {
    position: absolute;
    left: 34px; top: 120px;
    list-style: none;
    font-size: 14px;
    font-weight: 400;
    line-height: 25px;
    color: var(--ink);
  }
  .contact__phone--us { padding-left: 54px; }
  .band {
    position: absolute;
    left: 0; top: 218px;
    width: 520px; height: 46px;
    background: var(--navy);
  }
  .band__person {
    position: absolute;
    right: 30px; top: 4px;
    text-align: left;
    font-size: 13px;
    letter-spacing: 1px;
    line-height: 19px;
    color: var(--band-text);
  }

  /* Back */
  .card--back {
    background: var(--navy);
    display: flex;
    align-items: center;
    justify-content: center;
  }
  .monogram {
    font-size: 64px;
    font-weight: 400;
    letter-spacing: 8px;
    color: var(--stone-light);
  }
</style>
</head>
<body>
  <section class="card card--front">
    <div class="card__map" role="img" aria-label="Grey map of North and South America"></div>
    <div class="wordmark">
      <div class="wordmark__name">TOLVANE</div>
      <div class="wordmark__rule"></div>
      <div class="wordmark__legal">tttolvane sa, llc</div>
    </div>
    <ul class="contact">
      <li class="contact__phone--us">USA: +1 (555) 014 2200</li>
      <li>Guatemala: +1 (555) 014 2200</li>
      <li>email@tttolvane.com</li>
      <li>www.tttolvane.com</li>
    </ul>
    <div class="band">
      <div class="band__person">
        <div class="band__name">NAME</div>
        <div class="band__position">POSITION</div>
      </div>
    </div>
  </section>

  <section class="card card--back">
    <div class="monogram">TTT</div>
  </section>
</body>
</html>
```